Moravel Stenwick Inc needs a business card design

Looking for a unique, classy and sharp business card design.

Contact Information for Business Card

Moravel Stenwick Inc.
Marisa Ortega Bellido BScOT(c)
Occupational Therapist
(780) 555-0142
moravelstenwick@postlynx.net

```html
<!DOCTYPE html>
<html lang="en">
<head>
<meta charset="utf-8">
<title>Moravel Stenwick Inc. – Business Card</title>
<link rel="stylesheet" href="https://fonts.googleapis.com/css2?family=Roboto:wght@400;500;700&family=Roboto+Condensed:wght@500;700&display=swap">
<style>
  :root {
    --backdrop: #e9e9e8;
    --card-white: #f6f6f5;
    --plum: #8a2387;
    --leaf: #7dba3a;
    --ink: #444444;
    --divider: #c9c9c9;
    --white: #ffffff;
  }
  * { box-sizing: border-box; margin: 0; padding: 0; }
  html, body { width: 1200px; height: 960px; overflow: hidden; }
  body {
    background: var(--backdrop);
    font-family: "Roboto", Arial, sans-serif;
    position: relative;
  }
  .card {
    position: absolute;
    width: 601px;
    height: 343px;
    box-shadow: 0 2px 4px rgba(0,0,0,0.25);
    overflow: hidden;
  }
  .card-front { left: 314px; top: 113px; background: var(--card-white); }
  .card-back { left: 311px; top: 472px; background: var(--plum); }

  .front-wordmark {
    position: absolute;
    left: 30px; top: 150px;
    width: 236px;
    display: flex; align-items: center; justify-content: center; gap: 8px;
    color: var(--plum);
    font-weight: 700;
    font-size: 21px;
    white-space: nowrap;
  }
  .wordmark-dot {
    width: 12px; height: 12px; border-radius: 50%;
    background: var(--leaf);
    flex: none;
  }
  .front-divider {
    position: absolute;
    left: 284px; top: 82px;
    width: 1px; height: 183px;
    background: var(--divider);
  }
  .contact-block { position: absolute; left: 313px; top: 96px; }
  .holder-name {
    font-family: "Roboto Condensed", Arial, sans-serif;
    font-weight: 700; font-size: 19px;
    color: var(--plum);
    line-height: 26px;
  }
  .holder-role {
    font-family: "Roboto Condensed", Arial, sans-serif;
    font-weight: 500; font-size: 16px;
    color: var(--leaf);
    line-height: 24px;
    margin-top: 1px;
  }
  .company-name {
    font-size: 14px; color: var(--ink);
    margin-top: 14px; line-height: 20px;
  }
  .contact-list { list-style: none; margin-top: 6px; }
  .contact-list li {
    display: flex; align-items: center; gap: 9px;
    font-size: 14px; color: var(--ink);
    line-height: 19.5px;
  }
  .contact-list svg { width: 12px; height: 12px; fill: var(--plum); flex: none; }

  .front-band {
    position: absolute; left: 0; bottom: 0;
    width: 100%; height: 23px;
  }

  .back-wordmark {
    position: absolute;
    left: 0; top: 190px; width: 100%;
    display: flex; align-items: center; justify-content: center; gap: 10px;
    color: var(--white);
    font-weight: 700; font-size: 34px;
    white-space: nowrap;
  }
  .back-wordmark .wordmark-dot { width: 16px; height: 16px; background: var(--white); }
  .back-url {
    position: absolute;
    left: 0; top: 294px; width: 100%;
    text-align: center;
    color: var(--white);
    font-size: 14px;
    letter-spacing: 4.3px;
  }
</style>
</head>
<body>
  <section class="card card-front">
    <div class="front-wordmark"><span class="wordmark-dot"></span>Moravel Stenwick Inc</div>
    <div class="front-divider"></div>
    <div class="contact-block">
      <p class="holder-name">Marisa Ortega Bellido BScOT(c)</p>
      <p class="holder-role">Occupational Therapist</p>
      <p class="company-name">Moravel Stenwick Inc.</p>
      <ul class="contact-list">
        <li>
          <svg viewBox="0 0 24 24" aria-hidden="true"><path d="M6.6 10.8a15.1 15.1 0 0 0 6.6 6.6l2.2-2.2a1 1 0 0 1 1-.25 11.4 11.4 0 0 0 3.6.57 1 1 0 0 1 1 1V20a1 1 0 0 1-1 1A17 17 0 0 1 3 4a1 1 0 0 1 1-1h3.5a1 1 0 0 1 1 1c0 1.25.2 2.45.57 3.57a1 1 0 0 1-.25 1z"/></svg>
          (780) 555-0142
        </li>
        <li>
          <svg viewBox="0 0 24 24" aria-hidden="true"><path d="M2 5h20v2.2l-10 6.3L2 7.2z M2 9.6l10 6.3 10-6.3V19H2z"/></svg>
          moravelstenwick@postlynx.net
        </li>
        <li>
          <svg viewBox="0 0 24 24" aria-hidden="true"><circle cx="12" cy="12" r="10"/><path d="M7 7c2 0 3 1 3 2.5S8 12 9 14s-1 4-1 4M15 4c-1 2 0 3 1.5 3.5S19 10 17 12s-1 5 1 6" stroke="#f6f6f5" stroke-width="1.6" fill="none"/></svg>
          www.moravelstenwick.com
        </li>
      </ul>
    </div>
    <svg class="front-band" viewBox="0 0 601 23" preserveAspectRatio="none" aria-hidden="true">
      <polygon points="0,0 392,0 386,23 0,23" fill="var(--plum)"/>
      <polygon points="395,0 601,0 601,23 389,23" fill="var(--leaf)"/>
    </svg>
  </section>

  <section class="card card-back">
    <div class="back-wordmark"><span class="wordmark-dot"></span>Moravel Stenwick Inc</div>
    <p class="back-url">www.moravelstenwick.com</p>
  </section>
</body>
</html>
```